Banner for promote service of debit card

We are PagoVela and we need the banners to be posted on the facebook and instagram pages.
We want something to communicate that it is an exclusive debit card full of services.
Low commissions.
Our competitors:
https://www.kelvopay.com/it/home.html
https://www.drolo.com/it/
https://www.fotoreelix.com/sereqobank/
zephrolinko
maybe some banner that makes the idea of a convenient debit card that everyone can use.
Girls enjoying card shopping.
Please check also website for slogans and phrases to use
https://www.pagovela-app.com/
Should show the services.
We must convey that it is a fast, simple card that guarantees privacy.
We need strong banners that attract people as these ban will be sponsored on instagram and facebook
Target Market(s)
People 18-35 y
Open Bank account. low commissions. Easy to use. No limits. 100% Privacy.
Requirements
Must have
- Written in Italian.

```html
<!DOCTYPE html>
<html lang="it">
<head>
<meta charset="utf-8">
<title>PagoVela – Banner carta di debito</title>
<link rel="stylesheet" href="https://fonts.googleapis.com/css2?family=Montserrat:wght@300;400;600;800&display=swap">
<style>
  :root {
    --coral: #ff5a41;
    --sun: #f9c54b;
    --teal: #55cad5;
    --white: #ffffff;
    --ink-soft: #6b6b6b;
    --page: #ffffff;
  }
  html, body {
    margin: 0;
    padding: 0;
    width: 1200px;
    height: 1000px;
    overflow: hidden;
    background: var(--page);
  }
  .canvas {
    position: relative;
    width: 1200px;
    height: 1000px;
  }
  .banner {
    position: absolute;
    left: 224px;
    width: 780px;
    height: 409px;
    display: block;
  }
  .banner--sun { top: 59px; }
  .banner--teal { top: 510px; }

  .coral { fill: var(--coral); }
  .sun { fill: var(--sun); }
  .teal { fill: var(--teal); }
  .tab { fill: var(--white); }
  .brand-dot { fill: var(--coral); }

  .brand-name {
    font-family: "Montserrat", sans-serif;
    font-weight: 600;
    font-size: 17px;
    fill: var(--ink-soft);
  }
  .headline {
    font-family: "Montserrat", sans-serif;
    font-weight: 800;
    fill: var(--white);
  }
  .headline--xl { font-size: 74px; letter-spacing: -1px; }
  .headline--md { font-size: 31px; }
  .headline--lg { font-size: 44px; }
  .body-copy {
    font-family: "Montserrat", sans-serif;
    font-weight: 300;
    font-size: 30px;
    fill: var(--white);
  }
</style>
</head>
<body>
<div class="canvas">

  <!-- Banner 1: All in one -->
  <svg class="banner banner--sun" viewBox="0 0 1300 681" xmlns="http://www.w3.org/2000/svg">
    <defs>
      <linearGradient id="photoSun" x1="0" y1="0" x2="0" y2="1">
        <stop offset="0" stop-color="#d99a4a"/>
        <stop offset="0.35" stop-color="#e8e36a"/>
        <stop offset="1" stop-color="#f1d94a"/>
      </linearGradient>
    </defs>
    <rect class="sun" x="0" y="0" width="1300" height="681"/>
    <path class="coral" d="M0 0 H560 C640 180 640 500 560 681 H0 Z"/>

    <rect role="img" aria-label="Foto: ragazza sorridente in camicia gialla che tiene una carta davanti all'occhio" x="195" y="20" width="405" height="661" rx="40" fill="url(#photoSun)"/>

    <g class="brand-tab">
      <path class="tab" d="M1168 33 H1300 V124 H1168 A45.5 45.5 0 0 1 1168 33 Z"/>
      <circle class="brand-dot" cx="1211" cy="66" r="13"/>
      <text class="brand-name" x="1211" y="100" text-anchor="middle">PagoVela</text>
    </g>

    <text class="headline headline--xl" x="1246" y="318" text-anchor="end">All in one.</text>
    <text class="headline headline--md" x="1246" y="378" text-anchor="end">La carta adatta alla tue esigenze:</text>
    <text class="body-copy" x="1246" y="424" text-anchor="end">Veloce, Internazionale, Semplice.</text>
  </svg>

  <!-- Banner 2: La carta adatta -->
  <svg class="banner banner--teal" viewBox="0 0 1300 681" xmlns="http://www.w3.org/2000/svg">
    <defs>
      <linearGradient id="photoTeal" x1="0" y1="0" x2="0" y2="1">
        <stop offset="0" stop-color="#e07a34"/>
        <stop offset="0.4" stop-color="#e6743f"/>
        <stop offset="1" stop-color="#e5481f"/>
      </linearGradient>
      <linearGradient id="terminalTeal" x1="0" y1="0" x2="1" y2="0">
        <stop offset="0" stop-color="#3d4a55"/>
        <stop offset="1" stop-color="#e9b99c"/>
      </linearGradient>
    </defs>
    <rect class="teal" x="0" y="0" width="1300" height="681"/>
    <path class="coral" d="M0 0 H560 C640 180 640 500 560 681 H0 Z"/>

    <rect role="img" aria-label="Foto: ragazza in maglia arancione che porge una carta" x="145" y="12" width="420" height="669" rx="40" fill="url(#photoTeal)"/>
    <rect role="img" aria-label="Foto: mano che tiene un terminale di pagamento" x="800" y="480" width="500" height="165" rx="40" fill="url(#terminalTeal)"/>

    <g class="brand-tab">
      <path class="tab" d="M1168 38 H1300 V129 H1168 A45.5 45.5 0 0 1 1168 38 Z"/>
      <circle class="brand-dot" cx="1211" cy="71" r="13"/>
      <text class="brand-name" x="1211" y="105" text-anchor="middle">PagoVela</text>
    </g>

    <text class="headline headline--lg" x="1239" y="288" text-anchor="end">La carta adatta</text>
    <text class="headline headline--lg" x="1239" y="343" text-anchor="end">alla tue esigenze:</text>
    <text class="body-copy" x="1243" y="395" text-anchor="end">Transazioni istantanee, costi bassi</text>
    <text class="body-copy" x="1243" y="437" text-anchor="end">e facile da ricaricare.</text>
  </svg>

</div>
</body>
</html>
```